Real Estate Website

Please design a real estate website

The menu needs to be :
Home
About us
Houses for sale
Land for sale
Sold properties
Holiday accommodation
Rentals
Consumer affairs
Contact us.

Contact details to show in the footer:
Pinecrest Real Estate
27 Hollowmere Drive
Golden Beach 3851
03 5290 7741

Please add a 'contact us' form in the footer like on https://www.quillbrookestate.com.au/

Design of site should be a photo/slideshow please make it a lifestyle shot and use a photo from a google image search of 'golden beach victoria australia' as a placeholder.

Under this needs to be a section for a heading and description with about us button.

Further under this should be 6 feature properties like https://www.marlowvaleproperty.com.au/ and then under that a 'book a free appraisal' banner like the one on https://www.marlowvaleproperty.com.au/

Attached is the business logo

```html
<!DOCTYPE html>
<html lang="en">
<head>
<meta charset="utf-8">
<title>Pinecrest Real Estate</title>
<link href="https://fonts.googleapis.com/css2?family=Roboto:wght@400;500;700&family=Nunito+Sans:wght@400;600&display=swap" rel="stylesheet">
<style>
:root{
  --red:#c61f2e;
  --blue:#0b5aa5;
  --navy:#0f1a3b;
  --ink:#1b1f2a;
  --muted:#4a5060;
  --tan:#c9aa72;
  --sky:#86a5e2;
  --sea:#2aa9d2;
  --white:#ffffff;
}
*{box-sizing:border-box;margin:0;padding:0}
html,body{width:1200px;height:2232px;overflow:hidden}
body{position:relative;font-family:"Roboto",sans-serif;color:var(--ink);background:#fff}
.abs{position:absolute}

/* header */
.site-header{left:0;top:0;width:1200px;height:75px;background:linear-gradient(#ffffff,#eef2f9);z-index:5;box-shadow:0 1px 3px rgba(0,0,0,.08)}
.brand{left:24px;top:22px;display:flex;align-items:center;gap:6px}
.brand-mark{width:14px;height:14px;background:var(--blue);border-radius:50%}
.brand-name{font-weight:700;font-size:14px;color:var(--blue);line-height:1.1;width:90px}
.main-nav{left:323px;top:28px;display:flex;gap:24px;font-weight:500;font-size:13px;color:var(--ink)}
.main-nav span{display:flex;align-items:center;gap:4px}
.main-nav svg{width:11px;height:7px}
.btn-contact{left:1047px;top:19px;width:128px;height:37px;background:var(--red);color:#fff;font-weight:700;font-size:15px;border-radius:4px;display:flex;align-items:center;justify-content:center;box-shadow:0 2px 4px rgba(0,0,0,.2)}
.dropdown{left:406px;top:75px;width:150px;height:75px;background:#e7ebf3;border-radius:0 0 5px 5px;z-index:6;box-shadow:0 2px 6px rgba(0,0,0,.15);font-weight:500;font-size:13px}
.dropdown div{height:37px;display:flex;align-items:center;justify-content:center}
.dropdown div:first-child{background:#f1f4f9}

/* hero */
.hero{left:0;top:75px;width:1200px;height:425px;background:linear-gradient(180deg,var(--sky) 0%,var(--sea) 100%)}
.hero-title{left:225px;top:247px;width:531px;height:99px;background:rgba(90,96,110,.55);border-radius:4px;padding:11px 28px;color:#fff;font-weight:700;font-size:30px;line-height:38px}
.arrow{top:276px;width:16px;height:42px}
.tabs{left:250px;top:437px;display:flex;gap:2px}
.tab{width:114px;height:38px;border-radius:5px 5px 0 0;background:#e8eaef;color:#6a6f7a;font-weight:500;font-size:21px;display:flex;align-items:center;justify-content:center;border:1px solid #d8c9a5;border-bottom:none}
.tab.is-active{background:#fff;color:var(--ink)}
.search{left:225px;top:475px;width:750px;height:49px;background:#fff;border:1px solid #d8c9a5;border-radius:3px;box-shadow:0 2px 5px rgba(0,0,0,.1)}
.search-placeholder{left:24px;top:13px;font-family:"Nunito Sans",sans-serif;font-size:19px;color:#8b909b}
.btn-search{left:594px;top:4px;width:150px;height:40px;background:var(--red);border-radius:3px;color:#fff;font-weight:500;font-size:15px;display:flex;align-items:center;justify-content:center;gap:6px}
.filters{left:250px;top:524px;width:700px;height:38px;background:#fff;border:1px solid #d8c9a5;border-top:none;border-radius:0 0 4px 4px;box-shadow:0 2px 5px rgba(0,0,0,.1);font-family:"Nunito Sans",sans-serif;font-size:11px;color:#555}
.filters span{position:absolute;top:11px}
.filters .val{color:var(--blue)}
.filters .more{color:var(--blue);text-decoration:underline}

/* about */
.about{left:0;top:562px;width:1200px;height:569px;background:linear-gradient(#fbfcfe,#dfe7f2)}
.section-title{font-weight:500;font-size:26px;color:var(--red)}
.rule{height:2px;background:var(--blue);width:64px}
.about-text{left:225px;top:140px;width:385px;font-family:"Nunito Sans",sans-serif;font-size:14px;line-height:22.5px;color:var(--muted)}
.about-text p{margin-bottom:11px}
.signature{left:463px;top:489px;font-weight:700;font-size:15px;color:var(--ink)}
.team-photo{left:650px;top:281px;width:325px;height:225px;background:linear-gradient(135deg,#6f7a83,#1f242b)}

/* featured */
.featured{left:0;top:1131px;width:1200px;height:467px;background:linear-gradient(#fdfdfd,#f6f3ee)}
.card{width:224px;height:124px;border-radius:3px;overflow:hidden;border:2px solid #e6dccb;box-shadow:0 2px 4px rgba(0,0,0,.15)}
.photo-house{background:linear-gradient(180deg,#d3bfd6,#4e5a78)}
.photo-land{background:linear-gradient(180deg,#5a9ae0,#7fae45)}
.photo-pool{background:linear-gradient(180deg,#cfd8de,#2a9bcc)}
.card .count{left:6px;top:6px;font-size:9px;color:var(--red);display:flex;align-items:center;gap:2px}
.card .loc{right:0;top:12px;background:var(--blue);color:#fff;font-weight:500;font-size:12px;padding:3px 10px}
.card .price{right:0;top:36px;background:var(--red);color:#fff;font-weight:700;font-size:9.5px;padding:3px 8px}
.card .name{left:12px;top:86px;width:198px;height:18px;background:#fff;color:var(--red);font-size:12px;display:flex;align-items:center;justify-content:center}
.card .meta{left:22px;top:104px;width:178px;height:14px;background:rgba(255,255,255,.88);font-size:9px;color:#2a3d70;display:flex;justify-content:space-between;padding:0 10px;align-items:center}

/* appraisal band */
.appraisal{left:0;top:1598px;width:1200px;height:164px;background:var(--blue)}
.appraisal h2{position:absolute;left:225px;top:64px;font-weight:700;font-size:21px;color:#fff}
.appraisal p{position:absolute;left:225px;top:92px;font-family:"Nunito Sans",sans-serif;font-size:14px;color:#dfe8f5}
.btn-appraisal{left:739px;top:64px;width:236px;height:37px;background:var(--tan);border-radius:3px;color:#fff;font-weight:700;font-size:15px;display:flex;align-items:center;justify-content:center;box-shadow:0 2px 4px rgba(0,0,0,.2)}

/* footer */
.site-footer{left:0;top:1762px;width:1200px;height:470px;background:var(--navy);color:#fff}
.footer-brand{left:227px;top:95px;width:172px;text-align:center;font-weight:700;font-size:19px;line-height:1.15}
.social-dot{left:306px;top:182px;width:12px;height:12px;border:1.5px solid #aab2c6;border-radius:50%}
.footer-contact{left:237px;font-size:15px;line-height:22px;display:flex;gap:10px}
.footer-contact svg{width:18px;height:18px;flex:none;margin-top:2px}
.footer-links{left:487px;top:68px;font-weight:500;font-size:15px;line-height:37.6px;color:#e6e9f1}
.footer-form{left:737px;top:68px;width:225px}
.footer-form h3{font-weight:500;font-size:15px;margin-bottom:20px}
.field{background:#fff;border:1px solid #d8c9a5;border-radius:3px;height:24px;font-family:"Nunito Sans",sans-serif;font-size:11px;color:#8a8f99;padding:4px 9px;margin-bottom:7px;position:relative}
.field.short{width:150px}
.field.message{height:74px}
.field svg{position:absolute;right:8px;top:8px;width:9px;height:6px}
.btn-send{width:126px;height:24px;background:var(--red);border-radius:3px;color:#fff;font-weight:700;font-size:12px;display:flex;align-items:center;justify-content:center}
.footer-rule{left:225px;top:406px;width:750px;height:1px;background:#4a5370}
.legal{top:435px;font-size:7px;color:#b9bfcd}
</style>
</head>
<body>

<header class="site-header abs">
  <div class="brand abs"><span class="brand-mark"></span><span class="brand-name">Pinecrest Real Estate</span></div>
  <nav class="main-nav abs">
    <span>Home</span>
    <span>About Us</span>
    <span>Buy <svg viewBox="0 0 11 7"><path d="M1 6l4.5-4.5L10 6" fill="none" stroke="#1b1f2a" stroke-width="1.5"/></svg></span>
    <span>Rent <svg viewBox="0 0 11 7"><path d="M1 1l4.5 4.5L10 1" fill="none" stroke="#1b1f2a" stroke-width="1.5"/></svg></span>
    <span>Sell <svg viewBox="0 0 11 7"><path d="M1 1l4.5 4.5L10 1" fill="none" stroke="#1b1f2a" stroke-width="1.5"/></svg></span>
    <span>Sold Properties</span>
    <span>Consumer Affairs</span>
  </nav>
  <div class="btn-contact abs">Contact Us</div>
</header>

<div class="dropdown abs">
  <div>Houses for Sale</div>
  <div>Land for Sale</div>
</div>

<section class="hero abs" role="img" aria-label="Aerial photo of Golden Beach coastline with dunes, white sand and turquoise sea">
  <h1 class="hero-title abs">Beautiful beachfront property at Golden Beach, Victoria, Australia</h1>
  <svg class="arrow abs" style="left:11px" viewBox="0 0 16 42"><path d="M14 2L2 21l12 19" fill="none" stroke="#fff" stroke-width="2"/></svg>
  <svg class="arrow abs" style="left:1173px" viewBox="0 0 16 42"><path d="M2 2l12 19L2 40" fill="none" stroke="#fff" stroke-width="2"/></svg>
</section>

<div class="tabs abs">
  <div class="tab is-active">Buy</div>
  <div class="tab">Rent</div>
  <div class="tab">Sell</div>
</div>

<div class="search abs">
  <span class="search-placeholder abs">Search Suburbs</span>
  <div class="btn-search abs">
    <svg width="16" height="16" viewBox="0 0 16 16"><circle cx="7" cy="7" r="5.5" fill="none" stroke="#fff" stroke-width="1.6"/><path d="M11 11l4 4" stroke="#fff" stroke-width="1.6"/></svg>Search
  </div>
</div>

<div class="filters abs">
  <span class="val" style="left:26px">All Property Types ⌵</span>
  <span style="left:184px">Bedrooms</span>
  <span class="val" style="left:248px">2 ⌵</span>
  <span style="left:280px">to</span>
  <span class="val" style="left:302px">Any ⌵</span>
  <span style="left:385px">Budget</span>
  <span class="val" style="left:433px">$200,000 ⌵</span>
  <span style="left:505px">to</span>
  <span class="val" style="left:527px">Any ⌵</span>
  <span class="more" style="left:610px">More Filters</span>
</div>

<section class="about abs">
  <h2 class="section-title abs" style="left:225px;top:75px">About Us</h2>
  <div class="rule abs" style="left:225px;top:111px"></div>
  <div class="about-text abs">
    <p>Lorem ipsum dolor sit amet, consectetur adipiscing elit, sed do eiusmod tempor incididunt ut labore et dolore magna aliqua. Ut enim ad minim veniam, quis nostrud exercitation ullamco laboris nisi ut aliquip ex ea commodo consequat.</p>
    <p>Lorem ipsum dolor sit amet, consectetur adipiscing elit, sed do eiusmod tempor incididunt ut labore et dolore magna aliqua. Ut enim ad minim veniam, quis nostrud exercitation ullamco laboris nisi ut aliquip ex ea commodo consequat.</p>
    <p>Lorem ipsum dolor sit amet, consectetur adipiscing elit, sed do eiusmod tempor incididunt ut labore et dolore magna aliqua. Ut enim ad minim veniam, quis nostrud exercitation ullamco laboris nisi ut aliquip ex ea commodo consequat.</p>
  </div>
  <div class="signature abs">- Marcus Ellery</div>
  <div class="team-photo abs" role="img" aria-label="Team photo of the agency staff in business attire in a modern office"></div>
</section>

<section class="featured abs">
  <h2 class="section-title abs" style="left:0;width:1200px;text-align:center;top:56px">Our featured properties</h2>
  <div class="rule abs" style="left:568px;top:97px"></div>

  <article class="card photo-house abs" style="left:238px;top:130px" role="img" aria-label="Photo of a two-storey villa at dusk">
    <span class="count abs">▣ 15</span><span class="loc abs">Golden Beach, VIC</span><span class="price abs">$230,000</span>
    <span class="name abs">Villa overlooking Golden Beach</span><span class="meta abs"><span>300 sq. m.</span><span>2 Bedroom</span></span>
  </article>
  <article class="card photo-land abs" style="left:488px;top:130px" role="img" aria-label="Photo of a grassy plot with a single tree">
    <span class="count abs">▣ 7</span><span class="loc abs">Golden Beach, VIC</span><span class="price abs">$1,250,000</span>
    <span class="name abs">15 Hectare Plot</span><span class="meta abs"><span>15 Ha</span><span></span></span>
  </article>
  <article class="card photo-pool abs" style="left:738px;top:130px" role="img" aria-label="Photo of a villa terrace with infinity pool overlooking the sea">
    <span class="count abs">▣ 25</span><span class="loc abs">Golden Beach, VIC</span><span class="price abs">$230,000</span>
    <span class="name abs">Villa overlooking Golden Beach</span><span class="meta abs"><span>350 sq. m.</span><span>3 Bedroom</span></span>
  </article>
  <article class="card photo-house abs" style="left:238px;top:280px" role="img" aria-label="Photo of a two-storey villa at dusk">
    <span class="count abs">▣ 15</span><span class="loc abs">Golden Beach, VIC</span><span class="price abs">$230,000</span>
    <span class="name abs">Villa overlooking Golden Beach</span><span class="meta abs"><span>300 sq. m.</span><span>2 Bedroom</span></span>
  </article>
  <article class="card photo-house abs" style="left:488px;top:280px" role="img" aria-label="Photo of a two-storey villa at dusk">
    <span class="count abs">▣ 15</span><span class="loc abs">Golden Beach, VIC</span><span class="price abs">$230,000</span>
    <span class="name abs">Villa overlooking Golden Beach</span><span class="meta abs"><span>300 sq. m.</span><span>2 Bedroom</span></span>
  </article>
  <article class="card photo-house abs" style="left:738px;top:280px" role="img" aria-label="Photo of a two-storey villa at dusk">
    <span class="count abs">▣ 15</span><span class="loc abs">Golden Beach, VIC</span><span class="price abs">$230,000</span>
    <span class="name abs">Villa overlooking Golden Beach</span><span class="meta abs"><span>300 sq. m.</span><span>2 Bedroom</span></span>
  </article>
</section>

<section class="appraisal abs">
  <h2>Sell your property with Pinecrest Real Estate</h2>
  <p>We are the premier real estate agency for Golden Beach, Victoria, Australia</p>
  <div class="btn-appraisal abs">Book a Free Appraisal</div>
</section>

<footer class="site-footer abs">
  <div class="footer-brand abs">Pinecrest Real Estate</div>
  <span class="social-dot abs"></span>
  <div class="footer-contact abs" style="top:223px">
    <svg viewBox="0 0 18 18"><path d="M4 1.5l3 3-1.6 2.2c1 2.2 2.7 3.9 4.9 4.9L12.5 10l3 3-2 2.5C7.5 15 3 10.5 2.5 4z" fill="#fff"/></svg>
    <strong>03 5290 7741</strong>
  </div>
  <div class="footer-contact abs" style="top:256px">
    <svg viewBox="0 0 18 18"><path d="M9 1a5 5 0 0 1 5 5c0 3.8-5 10-5 10S4 9.8 4 6a5 5 0 0 1 5-5z" fill="#fff"/><circle cx="9" cy="6" r="1.8" fill="#0f1a3b"/></svg>
    <span>Pinecrest Real Estate<br>27 Hollowmere Drive<br>Golden Beach 3851</span>
  </div>

  <nav class="footer-links abs">
    <div>Home</div><div>About Us</div><div>Houses for Sale</div><div>Land for Sale</div>
    <div>Sold Properties</div><div>Holiday Accommodation</div><div>Rentals</div><div>Consumer Affairs</div>
  </nav>

  <form class="footer-form abs">
    <h3>Contact Us</h3>
    <div class="field">Your Name*</div>
    <div class="field">Your Email*</div>
    <div class="field short">Your Phone Number*</div>
    <div class="field message">Enter your message</div>
    <div class="field">Where did your hear about us?<svg viewBox="0 0 9 6"><path d="M1 1l3.5 3.5L8 1" fill="none" stroke="#666" stroke-width="1"/></svg></div>
    <div class="btn-send">Send Message</div>
  </form>

  <div class="footer-rule abs"></div>
  <div class="legal abs" style="left:225px">© 2021 Pinecrest Real Estate Pty Ltd. All Rights Reserved.</div>
  <div class="legal abs" style="left:855px">Privacy Policy | Terms and Conditions</div>
</footer>

</body>
</html>
```